Open Red Harbor.. a non profit that seeks to stomp out skin cancer .. quiet paths toward opening red

Simple letterhead incorporating logo

Industry/Entity Type

Non Profit

Font styles to use
Sans Serif

Colors

Designer to choose colors to be used in the design.

```html
<!DOCTYPE html>
<html lang="en">
<head>
<meta charset="utf-8">
<title>Open Red Harbor — Letterhead</title>
<link rel="stylesheet" href="https://fonts.googleapis.com/css2?family=Nunito:wght@400;700&display=swap">
<style>
  :root {
    --navy: #232945;
    --yellow: #f7e900;
    --paper: #ffffff;
    --backdrop: #ffffff;
    --text-light: #ffffff;
    --shadow: rgba(0, 0, 0, 0.35);
  }
  * { margin: 0; padding: 0; box-sizing: border-box; }
  html, body {
    width: 998px;
    height: 1200px;
    overflow: hidden;
    background: var(--backdrop);
  }
  .canvas {
    position: relative;
    width: 998px;
    height: 1200px;
  }
  .sheet {
    position: absolute;
    left: 138px;
    top: 66px;
    width: 757px;
    height: 1069px;
    background: var(--paper);
    box-shadow: 2px 3px 5px var(--shadow);
    overflow: hidden;
  }
  .header-band {
    position: absolute;
    left: 0;
    top: 0;
    width: 757px;
    height: 260px;
  }
  .brand-name-mark {
    position: absolute;
    left: 52px;
    top: 98px;
    width: 180px;
    text-align: center;
    font-family: "Nunito", sans-serif;
    font-weight: 400;
    font-size: 20px;
    line-height: 1;
    white-space: nowrap;
    color: var(--yellow);
  }
  .org-details {
    position: absolute;
    left: 239px;
    top: 78px;
    font-family: "Nunito", sans-serif;
    color: var(--text-light);
  }
  .org-name {
    font-weight: 700;
    font-size: 29px;
    letter-spacing: 4.4px;
    line-height: 1;
    margin-bottom: 10px;
    white-space: nowrap;
  }
  .org-contact {
    font-weight: 400;
    font-size: 13px;
    line-height: 15px;
    letter-spacing: 0.1px;
    white-space: nowrap;
  }
</style>
</head>
<body>
  <main class="canvas">
    <section class="sheet">
      <svg class="header-band" viewBox="0 0 757 260" aria-hidden="true">
        <path d="M0 0 H757 V114 Q430 335 0 197 Z" fill="var(--yellow)"/>
        <path d="M0 0 H757 V100 Q430 318 0 181 Z" fill="var(--navy)"/>
      </svg>
      <div class="brand-name-mark">Open Red Harbor</div>
      <header class="org-details">
        <h1 class="org-name">Open Red Harbor</h1>
        <p class="org-contact">215 Lantern St Keene, New Hampshire<br>03431 603-555-0148 ext 23</p>
      </header>
    </section>
  </main>
</body>
</html>
```